DEAN COLLOPY PROPERTY SERVICES

I want a business card that is clean and simple.
'Dean Collopy Property Services' is the title.
Somewhere on the card needs to be 'Carpentry, Tiling, painting and garden services'

On the back of card
PH 087 394 1526
email: deancollopypropertyservices@fernmail.net

I have attached a picture of my other business. I would like the font and design to be similar to the bathroom business.

Many thanks.

```html
<!DOCTYPE html>
<html lang="en">
<head>
<meta charset="utf-8">
<title>Dean Collopy Property Services – Business Card</title>
<link href="https://fonts.googleapis.com/css2?family=Open+Sans:ital,wght@0,300;0,400;0,600;1,400&display=swap" rel="stylesheet">
<style>
  :root {
    --page-bg: #f1f1f1;
    --silver-light: #fbfbfb;
    --silver-mid: #e6e6e6;
    --silver-dark: #cfcfcf;
    --ink: #161616;
    --card-black: #1a1818;
    --card-black-edge: #262323;
    --paper-white: #ffffff;
    --rule-grey: #6f6b6b;
  }
  * { margin: 0; padding: 0; box-sizing: border-box; }
  html, body {
    width: 1200px; height: 1200px; overflow: hidden;
    background: var(--page-bg);
    font-family: "Open Sans", Arial, sans-serif;
  }
  .sheet {
    width: 1200px; height: 1200px;
    display: flex; flex-direction: column;
    align-items: center; justify-content: center; gap: 70px;
  }
  .card {
    width: 760px; height: 440px; border-radius: 4px;
    box-shadow: 0 10px 30px rgba(0,0,0,0.12);
    position: relative;
  }
  /* Front */
  .card-front {
    background: linear-gradient(120deg, var(--silver-mid) 0%, var(--silver-light) 40%, var(--silver-dark) 55%, var(--silver-light) 75%, var(--silver-mid) 100%);
    display: flex; flex-direction: column; align-items: center; justify-content: center;
    color: var(--ink);
  }
  .brand-name {
    font-size: 46px; font-weight: 400; letter-spacing: 0.5px; line-height: 1.1;
  }
  .company-title {
    margin-top: 14px; font-size: 21px; font-weight: 400; letter-spacing: 1px; color: #2a2a2a;
  }
  /* Back */
  .card-back {
    background: linear-gradient(180deg, var(--card-black-edge) 0%, var(--card-black) 100%);
    color: var(--paper-white);
  }
  .contact-block {
    position: absolute; left: 50%; top: 110px; transform: translateX(-42%);
    text-align: center; width: 520px;
  }
  .person-name { font-size: 40px; font-weight: 400; letter-spacing: 2px; line-height: 1.1; }
  .person-role { font-size: 17px; font-weight: 600; margin-top: 2px; }
  .contact-line { font-size: 15px; font-weight: 400; margin-top: 10px; line-height: 1.35; }
  .contact-line + .contact-line { margin-top: 2px; }
  .divider { height: 1px; background: var(--rule-grey); margin: 12px 0 10px; }
  .services { font-size: 19px; font-style: italic; font-weight: 400; letter-spacing: 0.5px; }
</style>
</head>
<body>
  <main class="sheet">
    <section class="card card-front" aria-label="Card front">
      <div class="brand-name">Dean Collopy Bathrooms</div>
      <div class="company-title">DEAN COLLOPY PROPERTY SERVICES</div>
    </section>

    <section class="card card-back" aria-label="Card back">
      <div class="contact-block">
        <div class="person-name">DEAN COLLOPY</div>
        <div class="person-role">Owner</div>
        <div class="contact-line">087 394 1526</div>
        <div class="contact-line">deancollopypropertyservices@fernmail.net</div>
        <div class="divider"></div>
        <div class="services">Carpentry, Tiling, Painting And Garden Services</div>
      </div>
    </section>
  </main>
</body>
</html>
```